Website Design for Wheels for Heroes.org - Donated Cars to Disabled Vets

Need a Wordpress website. The coding now, esp. the CDONT coding is not supported by many hosting sites. Looking for a landing page to generate leads.

Logo Text

look at current one for ideas

Coding

Coded - Design and coding required

Number of Pages Required

1 page

Requirements
Must have
• look at current website at www.wheelsforheroes.org
Nice to have
• look at this site: http://givevehicletotroops.org

```html
<!DOCTYPE html>
<html lang="en">
<head>
<meta charset="utf-8">
<title>Wheels for Heroes – Donate Your Car</title>
<link rel="stylesheet" href="https://fonts.googleapis.com/css2?family=Open+Sans:wght@400;600;700;800&display=swap">
<style>
:root{
  --navy:#0f2a78;
  --blue:#1d3f9c;
  --blue-deep:#0b2266;
  --red:#b3141b;
  --red-deep:#8c0c10;
  --gold:#d8b56a;
  --ink:#1e2a4a;
  --text:#3b3b3b;
  --muted:#6b6b6b;
  --line:#d6d6d6;
  --frame:#e9e9e9;
  --white:#ffffff;
}
*{box-sizing:border-box;margin:0;padding:0}
html,body{width:1200px;height:2659px;overflow:hidden}
body{background:var(--frame);font-family:"Open Sans",Arial,sans-serif;color:var(--text);position:relative}
.abs{position:absolute}
svg{display:block}

/* header */
.site-header{left:14px;top:14px;width:1172px;height:151px;background:linear-gradient(100deg,#c9262b 0%,#a5141b 45%,#8a2c3a 70%,#b51a22 100%)}
.brand{left:49px;top:78px;display:flex;align-items:center;gap:12px}
.brand-mark{width:18px;height:18px;border-radius:50%;background:var(--gold)}
.brand-name{font-weight:800;font-size:30px;color:var(--white);letter-spacing:.5px;text-transform:uppercase}
.call{left:810px;top:52px;display:flex;align-items:center;gap:14px;color:var(--white)}
.call-icon{width:66px;height:66px;border:3px solid var(--white);border-radius:50%;display:flex;align-items:center;justify-content:center}
.call-label{font-weight:700;font-size:19px;line-height:1.1}
.call-number{font-weight:800;font-size:32px;line-height:1.1}
.call-note{font-weight:700;font-size:12px}

/* nav */
.site-nav{left:14px;top:165px;width:1172px;height:46px;background:var(--navy)}
.site-nav a{position:absolute;top:14px;color:var(--white);font-weight:700;font-size:15px;text-decoration:none;text-transform:uppercase}

/* hero */
.hero-photo{left:14px;top:211px;width:1172px;height:518px;background:linear-gradient(110deg,#1b2f6e 0%,#3a4a86 22%,#7a6f63 38%,#9a3034 60%,#c2333a 80%,#8e1f27 100%)}
.form-icon{left:947px;top:242px;width:34px;height:34px;border-radius:50%;background:var(--white);display:flex;align-items:center;justify-content:center}
.form-head{left:775px;top:263px;width:379px;height:51px;background:var(--red);color:var(--white);font-weight:700;font-size:20px;display:flex;align-items:center;justify-content:center;text-transform:uppercase}
.form-panel{left:789px;top:314px;width:351px;height:383px;background:rgba(245,245,245,.88)}
.form-sub{position:absolute;left:0;right:0;top:18px;text-align:center;color:var(--red);font-weight:700;font-size:15px}
.field{position:absolute;height:29px;background:var(--white);border:1px solid #cfcfcf;border-radius:3px;font-size:11.5px;color:#444;padding:6px 8px;font-weight:600}
.field.half{width:153px}
.field.full{width:316px}
.field.select::after{content:"";position:absolute;right:8px;top:11px;border:5px solid transparent;border-top:6px solid #555}
.field.select::before{content:"";position:absolute;right:26px;top:4px;bottom:4px;width:1px;background:#ccc}
.btn-donate{left:807px;top:628px;width:153px;height:41px;background:var(--red-deep);border-radius:4px;color:var(--white);font-weight:700;font-size:15px;display:flex;align-items:center;justify-content:center;text-transform:uppercase}

/* benefits band */
.benefits{left:14px;top:729px;width:1172px;height:193px;background:linear-gradient(90deg,#123384 0%,#2046a6 50%,#173a94 100%)}
.benefits-title{left:71px;top:760px;width:330px;text-align:center;color:var(--white);font-weight:800;text-transform:uppercase;line-height:1.05}
.benefits-title .l1,.benefits-title .l3{font-size:27px}
.benefits-title .l2{font-size:54px;color:var(--gold);letter-spacing:1px}
.benefit{position:absolute;top:771px;width:140px;text-align:center;color:var(--white)}
.benefit svg{margin:0 auto}
.benefit p{margin-top:18px;font-weight:700;font-size:13px;line-height:1.3}

/* how to donate */
.how{left:14px;top:922px;width:1172px;height:333px;background:var(--white)}
.section-title{position:absolute;left:14px;width:1172px;text-align:center;font-weight:800;font-size:28px;color:var(--navy);text-transform:uppercase}
.section-title em{font-style:normal;color:var(--red)}
.section-title.rule::before,.section-title.rule::after{content:"";display:inline-block;width:170px;height:1px;background:var(--line);vertical-align:middle;margin:0 30px}
.section-title.light{color:var(--white)}
.section-title.light::before,.section-title.light::after{background:rgba(255,255,255,.6);width:110px}
.step-icon{position:absolute;top:1050px}
.step h3{position:absolute;font-size:15px;font-weight:800;color:var(--navy);text-transform:uppercase;line-height:1.25}
.step p{position:absolute;font-size:13px;font-weight:600;color:#444;line-height:1.4}

/* why donate */
.why{left:14px;top:1255px;width:1172px;height:486px;background:linear-gradient(180deg,#173a8f 0%,#2449a6 50%,#1a3c95 100%)}
.reason{position:absolute;width:470px;display:flex;gap:12px;color:var(--white);font-size:13.5px;line-height:1.3}
.reason b{font-weight:700}
.reason .dot{flex:none;width:26px;height:26px;border-radius:50%;background:var(--red);border:2px solid var(--white);display:flex;align-items:center;justify-content:center}
.vehicle-truck{left:165px;top:1573px;width:455px;height:180px;border-radius:40px 60px 22px 22px;background:linear-gradient(180deg,#3b3f45 0%,#15171a 70%,#0a0a0a 100%)}
.vehicle-coupe{left:700px;top:1611px;width:351px;height:165px;border-radius:70px 90px 24px 24px;background:linear-gradient(180deg,#e63a3f 0%,#b3141b 65%,#5a0a0d 100%)}

/* faq */
.faq{left:14px;top:1741px;width:1172px;height:627px;background:var(--white)}
.faq-photo{left:92px;top:1883px;width:507px;height:415px;background:linear-gradient(160deg,#2d3f7e 0%,#c9c4c3 35%,#b1242c 55%,#8a8274 75%,#6b5a48 100%)}
.faq-item{position:absolute;left:633px;width:475px;border:1px solid #cdcdcd;border-radius:10px;background:var(--white);padding:9px 14px;box-shadow:0 1px 2px rgba(0,0,0,.12)}
.faq-item h4{font-size:14px;font-weight:700;color:var(--ink);position:relative}
.faq-item h4::after{content:"";position:absolute;right:2px;top:4px;width:7px;height:7px;border-right:2px solid #333;border-bottom:2px solid #333;transform:rotate(45deg)}
.faq-item.open h4::after{transform:rotate(-135deg);top:8px}
.faq-item p{margin-top:8px;font-size:12.5px;line-height:1.5;color:#555}

/* footer */
.site-footer{left:14px;top:2368px;width:1172px;height:249px;background:linear-gradient(100deg,#c0242a 0%,#a7141b 50%,#b41c23 100%)}
.footer-brand{left:44px;top:2466px;display:flex;align-items:center;gap:10px}
.footer-brand .brand-name{font-size:24px}
.footer-col h5{position:absolute;color:var(--white);font-size:14px;font-weight:700;text-transform:uppercase;padding-bottom:10px;border-bottom:1px solid rgba(255,255,255,.6)}
.footer-about{left:413px;top:2441px;width:240px;font-size:11.5px;font-weight:600;line-height:1.55;color:var(--white)}
.footer-links{left:700px;top:2444px;list-style:none}
.footer-links li{font-size:12px;font-weight:700;color:var(--white);line-height:19.6px;text-transform:uppercase}
.footer-call{left:897px;top:2390px;width:264px;height:114px;border:2px solid var(--white);border-radius:6px;color:var(--white);text-align:center;padding-top:18px}
.footer-call .call-label{font-size:19px}
.footer-call .call-number{font-size:31px}
.copyright{left:14px;top:2617px;width:1172px;height:25px;background:var(--navy);color:var(--white);font-size:11px;font-weight:700;display:flex;align-items:center;justify-content:center;text-transform:uppercase}
</style>
</head>
<body>

<header class="abs site-header"></header>
<div class="abs brand"><span class="brand-mark"></span><span class="brand-name">Wheels for Heroes</span></div>
<div class="abs call">
  <div class="call-icon">
    <svg width="32" height="32" viewBox="0 0 24 24"><path fill="#fff" d="M6.6 10.8a15 15 0 0 0 6.6 6.6l2.2-2.2a1 1 0 0 1 1-.25 11.4 11.4 0 0 0 3.6.57 1 1 0 0 1 1 1V20a1 1 0 0 1-1 1A17 17 0 0 1 3 4a1 1 0 0 1 1-1h3.5a1 1 0 0 1 1 1c0 1.25.2 2.45.57 3.57a1 1 0 0 1-.25 1z"/></svg>
  </div>
  <div>
    <div class="call-label">CALL TODAY TO DONATE</div>
    <div class="call-number">1-800-555-0142</div>
    <div class="call-note">Live Operators Available - 7 Days A Week</div>
  </div>
</div>

<nav class="abs site-nav">
  <a style="left:349px">How to Donate</a>
  <a style="left:532px">Why Donate</a>
  <a style="left:688px">FAQ</a>
  <a style="left:771px">About</a>
</nav>

<div class="abs hero-photo" role="img" aria-label="Soldier in camouflage hugging a child holding a small flag, in front of a waving American flag"></div>
<div class="abs form-head">Donate Your Car Online Below</div>
<div class="abs form-icon"><svg width="20" height="14" viewBox="0 0 20 14"><path fill="#b3141b" d="M3 6l2-4.5h10L17 6h1.5a1 1 0 0 1 1 1v4h-2v2h-3v-2h-9v2h-3v-2h-2V7a1 1 0 0 1 1-1z"/></svg></div>
<form class="abs form-panel">
  <div class="form-sub">Full Tax Deduction - Running or Not</div>
  <div class="field half" style="left:17px;top:50px">First Name</div>
  <div class="field half" style="left:180px;top:50px">Last Name</div>
  <div class="field half" style="left:17px;top:87px">Daytime Phone</div>
  <div class="field half" style="left:180px;top:87px">Email</div>
  <div class="field full" style="left:17px;top:124px">Pickup Address</div>
  <div class="field full" style="left:17px;top:161px">Pickup City</div>
  <div class="field half select" style="left:17px;top:198px">Pickup State</div>
  <div class="field half" style="left:180px;top:198px">Zip Code</div>
  <div class="field half select" style="left:17px;top:235px">Choose Year</div>
  <div class="field half select" style="left:180px;top:235px">Choose Make</div>
  <div class="field full" style="left:17px;top:272px">Vehicle Model</div>
</form>
<div class="abs btn-donate">Donate Now</div>

<section class="abs benefits"></section>
<h2 class="abs benefits-title"><span class="l1">Donate Your Car to</span><br><span class="l2">Veterans</span><br><span class="l3">Make a Difference</span></h2>
<div class="benefit" style="left:447px">
  <svg width="54" height="54" viewBox="0 0 54 54"><circle cx="27" cy="27" r="24" fill="none" stroke="#8ec5ff" stroke-width="3"/><path d="M15 27l9 9 17-18" fill="none" stroke="#8ec5ff" stroke-width="4"/></svg>
  <p>You have<br>no costs</p>
</div>
<div class="benefit" style="left:584px">
  <svg width="60" height="54" viewBox="0 0 60 54"><rect x="6" y="20" width="30" height="20" rx="3" fill="#8ec5ff"/><path d="M36 26h10l8 8v6H36z" fill="#8ec5ff"/><circle cx="16" cy="44" r="6" fill="#fff"/><circle cx="46" cy="44" r="6" fill="#fff"/><path d="M14 20L24 4h6" stroke="#8ec5ff" stroke-width="3" fill="none"/></svg>
  <p>Free towing,<br>running or not</p>
</div>
<div class="benefit" style="left:724px">
  <svg width="44" height="54" viewBox="0 0 44 54"><rect x="4" y="3" width="36" height="48" rx="3" fill="none" stroke="#8ec5ff" stroke-width="3"/><path d="M12 16h20M12 24h20M12 32h20M12 40h12" stroke="#8ec5ff" stroke-width="3"/></svg>
  <p>We issue you an<br>IRS tax receipt</p>
</div>
<div class="benefit" style="left:866px">
  <svg width="50" height="54" viewBox="0 0 50 54"><rect x="8" y="3" width="32" height="44" rx="3" fill="none" stroke="#8ec5ff" stroke-width="3"/><circle cx="20" cy="38" r="9" fill="#1d3f9c" stroke="#8ec5ff" stroke-width="3"/><path d="M20 33v6M20 42v1" stroke="#8ec5ff" stroke-width="3"/><path d="M16 12h16M16 20h16" stroke="#8ec5ff" stroke-width="3"/></svg>
  <p>We take care of<br>all paperwork.</p>
</div>
<div class="benefit" style="left:1001px">
  <svg width="44" height="54" viewBox="0 0 44 54"><rect x="4" y="8" width="36" height="43" rx="3" fill="none" stroke="#8ec5ff" stroke-width="3"/><rect x="14" y="3" width="16" height="9" rx="2" fill="#8ec5ff"/><path d="M12 26h20M12 34h20M12 42h12" stroke="#8ec5ff" stroke-width="3"/></svg>
  <p>We take care of<br>DMV &amp; Smog issues</p>
</div>

<section class="abs how"></section>
<h2 class="section-title rule" style="top:976px">How to <em>Donate</em></h2>
<div class="step">
  <svg class="step-icon" style="left:88px" width="70" height="96" viewBox="0 0 70 96"><rect x="10" y="0" width="58" height="12" fill="#b3141b"/><rect x="10" y="20" width="58" height="12" fill="#b3141b"/><rect x="24" y="40" width="44" height="12" fill="#b3141b"/><path d="M4 90l20-34 8 20z" fill="#b3141b"/></svg>
  <h3 style="left:172px;top:1090px">Call us at 1-800-555-0142 or<br>fill out the online form</h3>
  <p style="left:172px;top:1134px;width:240px">Donating your vehicle is easy and donation is accepted nationwide.</p>
</div>
<div class="step">
  <svg class="step-icon" style="left:449px" width="96" height="80" viewBox="0 0 96 80"><rect x="4" y="28" width="40" height="30" rx="4" fill="#b3141b"/><path d="M44 36h20l16 16v6H44z" fill="#b3141b"/><path d="M24 28L52 4" stroke="#b3141b" stroke-width="6"/><circle cx="20" cy="64" r="9" fill="#fff" stroke="#b3141b" stroke-width="5"/><circle cx="66" cy="64" r="9" fill="#fff" stroke="#b3141b" stroke-width="5"/></svg>
  <h3 style="left:555px;top:1090px">We tow the vehicle</h3>
  <p style="left:555px;top:1124px;width:240px">Any vehicles is accepted and we will arrange to pick up your vehicle when it is most convenient for you.</p>
</div>
<div class="step">
  <svg class="step-icon" style="left:839px" width="70" height="92" viewBox="0 0 70 92"><rect x="14" y="2" width="50" height="80" fill="none" stroke="#b3141b" stroke-width="3"/><rect x="4" y="10" width="50" height="80" fill="#fff" stroke="#b3141b" stroke-width="3"/><text x="29" y="38" font-family="Open Sans,Arial,sans-serif" font-size="22" font-weight="800" fill="#b3141b" text-anchor="middle">$</text><path d="M12 50h34M12 60h34M12 70h34M24 50v28M36 50v28" stroke="#b3141b" stroke-width="2.5"/></svg>
  <h3 style="left:934px;top:1090px">Tax Write-Off</h3>
  <p style="left:934px;top:1124px;width:215px">Once the vehicle donation is complete, you will receive your tax deductable vehicle donation receipt.</p>
</div>

<section class="abs why"></section>
<h2 class="section-title rule light" style="top:1295px">Why Donate Your Car to Us</h2>
<div class="reason" style="left:64px;top:1382px"><span class="dot"><svg width="12" height="12" viewBox="0 0 12 12"><path d="M1 6h9M6 2l4 4-4 4" stroke="#fff" stroke-width="2" fill="none"/></svg></span><span><b>Top-Rated A+ &amp; IRS 501(c)3 Approved :</b> Free 24/7 Pickup with No DMV Hassles.</span></div>
<div class="reason" style="left:64px;top:1432px"><span class="dot"><svg width="12" height="12" viewBox="0 0 12 12"><path d="M1 6h9M6 2l4 4-4 4" stroke="#fff" stroke-width="2" fill="none"/></svg></span><span><b>Free Local Towing :</b> We will pick up your car donation, running or not, when it's most convenient, at home or work.</span></div>
<div class="reason" style="left:64px;top:1482px"><span class="dot"><svg width="12" height="12" viewBox="0 0 12 12"><path d="M1 6h9M6 2l4 4-4 4" stroke="#fff" stroke-width="2" fill="none"/></svg></span><span><b>All Cars Accepted :</b> We take your car regardless of its condition or registration status.</span></div>
<div class="reason" style="left:64px;top:1533px"><span class="dot"><svg width="12" height="12" viewBox="0 0 12 12"><path d="M1 6h9M6 2l4 4-4 4" stroke="#fff" stroke-width="2" fill="none"/></svg></span><span><b>Income Tax Deduction :</b> We issue you an IRS tax receipt &amp; offer the largest resale network to get you the highest tax write-off possible.</span></div>
<div class="reason" style="left:633px;top:1382px"><span class="dot"><svg width="12" height="12" viewBox="0 0 12 12"><path d="M1 6h9M6 2l4 4-4 4" stroke="#fff" stroke-width="2" fill="none"/></svg></span><span><b>No Paperwork Hassles :</b> We take any car and handle everything: DMV, Smog and IRS paperwork.</span></div>
<div class="reason" style="left:633px;top:1432px"><span class="dot"><svg width="12" height="12" viewBox="0 0 12 12"><path d="M1 6h9M6 2l4 4-4 4" stroke="#fff" stroke-width="2" fill="none"/></svg></span><span><b>Car donations help fund programs :</b> And benefit Allied Heroes Support Fund. An IRS 501(c)3 nonprofit organization.</span></div>
<div class="reason" style="left:633px;top:1482px"><span class="dot"><svg width="12" height="12" viewBox="0 0 12 12"><path d="M1 6h9M6 2l4 4-4 4" stroke="#fff" stroke-width="2" fill="none"/></svg></span><span><b>Schedule a Free Pickup :</b> Complete the form and a representative will call you to arrange a convenient time to pickup your car.</span></div>

<section class="abs faq"></section>
<div class="abs vehicle-truck" role="img" aria-label="Black full-size pickup truck"></div>
<div class="abs vehicle-coupe" role="img" aria-label="Red classic muscle car with white racing stripes"></div>
<h2 class="section-title rule" style="top:1808px">Frequently Asked <em>Questions</em></h2>
<div class="abs faq-photo" role="img" aria-label="Marching soldiers in camouflage beneath a large American flag"></div>
<div class="faq-item" style="top:1883px"><h4>What types of vehicles can be donated?</h4></div>
<div class="faq-item open" style="top:1929px"><h4>What paperwork do I need to donate my vehicle?</h4><p>All you need is a title, free of all liens. We will request some general information from you at the time of donation such as, the year, make, and model of the car, as well as its general mechanical condition. We accept all vehicles, running or non-running.</p></div>
<div class="faq-item" style="top:2086px"><h4>Is my donated vehicle tax -deductible?</h4></div>
<div class="faq-item" style="top:2132px"><h4>What if the vehicle is not registered in my name?</h4></div>
<div class="faq-item" style="top:2178px"><h4>How much will I receive as a tax deduction for my vehicle?</h4></div>
<div class="faq-item" style="top:2224px"><h4>When will I receive my tax receipt?</h4></div>
<div class="faq-item" style="top:2270px"><h4>How do I schedule a pick up?</h4></div>

<footer class="abs site-footer"></footer>
<div class="abs footer-brand"><span class="brand-mark"></span><span class="brand-name">Wheels for Heroes</span></div>
<div class="footer-col"><h5 style="left:413px;top:2402px;width:250px">About Wheels for Heroes</h5></div>
<p class="abs footer-about">Lorem ipsum dolor sit amet, consectetuer adipiscing elit, sed diam nonummy nibheu ismod tincidunt ut laoreet dolore magna aliquam erat volutpat. Ut wisi enim ad mini veniam, quis nostrud exerci tation ullamcor per suscipit lobortis nisl ut aliquip ex ea co modo consequat.</p>
<div class="footer-col"><h5 style="left:700px;top:2402px;width:150px">Navigation</h5></div>
<ul class="abs footer-links"><li>How to Donate</li><li>Why Donate</li><li>FAQ</li><li>About</li></ul>
<div class="abs footer-call">
  <div class="call-label">CALL TODAY TO DONATE</div>
  <div class="call-number">1-800-555-0142</div>
  <div class="call-note">Live Operators Available - 7 Days A Week</div>
</div>
<div class="abs copyright">Copyright © 2016 Wheels for Heroes. Privacy Policy | Terms &amp; Conditions. All rights reserved.</div>

</body>
</html>
```